Purely Windswept needs an eye catching marketing flyer

Our new Luminous Airflow(r) business needs an eye catching marketing flyer. We think A5 sizing?
website link (where you can understand more about breathwork is www.purelywindswept.co.uk)
Design whatever you would like to design some things that could be of use to mention are below. Will leave it in your capable hands.
Logo files for Purely Windswept attached, use whichever one is best for your design, should be the main logo and colour scheme for the flyer, the second logo is that of Luminous Airflow(r) the breath school who's body of work we will be delivering. This can be anywhere on the flyer
Flyer is needed to get people interested in breathwork, the potential benefits for breathing better
We offer 1:1 sessions, workshops, corporate training
The flyer will have an offer code 'OpenGlow' which will give 15% off the bookers first 1:1 session
Flyer should include the following contact details: Maybe a "find out how breathwork can help you today. . . "
Tessa Orchard (South): 07700 318 527
Lorraine Pitt (Midlands): 07700 452 183
facebook: we.are.purelywindswept
instagram: _purelywindswept_

```html
<!DOCTYPE html>
<html lang="en">
<head>
<meta charset="utf-8">
<title>Purely Windswept – Flyer</title>
<link rel="stylesheet" href="https://fonts.googleapis.com/css2?family=Jost:wght@400;600;700&family=Montserrat:wght@800&family=Oswald:wght@500&family=Roboto+Condensed:wght@400;700&family=Courgette&family=Dancing+Script:wght@700&display=swap">
<style>
  :root {
    --page-bg: #b1b1b1;
    --cream: #f1e9d6;
    --ink: #111111;
    --teal: #21969b;
    --green: #78a03c;
    --mustard: #d8bb2e;
    --orange: #e9560e;
    --white: #ffffff;
    --frame: #b9a6ee;
  }
  * { margin: 0; padding: 0; box-sizing: border-box; }
  html, body { width: 1200px; height: 1197px; overflow: hidden; background: var(--page-bg); }
  .flyer {
    position: absolute; left: 198px; top: 28px;
    width: 804px; height: 1140px; overflow: hidden;
    background: var(--cream);
  }
  .flyer-art { position: absolute; inset: 0; }
  .line { position: absolute; left: 0; width: 100%; text-align: center; white-space: nowrap; }

  .brand-name {
    position: absolute; left: 418px; top: 190px; width: 320px;
    text-align: center; color: var(--white);
    font-family: "Jost", sans-serif; font-weight: 400;
    font-size: 46px; line-height: 1.1;
  }

  .offer { position: absolute; left: 45px; top: 445px; width: 408px; height: 408px; color: var(--white); font-family: "Jost", sans-serif; }
  .offer-label { top: 105px; font-size: 46px; font-weight: 400; letter-spacing: 1px; }
  .offer-code { top: 157px; font-size: 42px; font-weight: 700; }
  .offer-amount { top: 195px; font-size: 62px; font-weight: 700; }
  .offer-terms { top: 272px; font-size: 31px; font-weight: 600; }
  .offer-session { top: 305px; font-size: 50px; font-weight: 600; }

  .services { position: absolute; left: 470px; top: 620px; width: 310px; text-align: center; }
  .services-title { font-family: "Courgette", cursive; font-style: italic; color: var(--teal); font-size: 62px; line-height: 1.05; }
  .services-list { list-style: none; font-family: "Montserrat", sans-serif; font-weight: 800; font-size: 33px; line-height: 35px; }
  .service--sessions { color: var(--green); }
  .service--workshops { color: var(--mustard); }
  .service--corporate { color: var(--orange); }

  .contact { position: absolute; left: 0; top: 900px; width: 804px; text-align: center; color: var(--ink); }
  .contact-cta { font-family: "Oswald", sans-serif; font-weight: 500; font-size: 33px; transform: scaleX(0.82); margin-bottom: 10px; }
  .contact-details { font-family: "Roboto Condensed", sans-serif; font-size: 18.5px; line-height: 25px; }
  .contact-details b { font-weight: 700; }
  .contact-web { font-family: "Dancing Script", cursive; font-weight: 700; font-size: 38px; margin-top: 8px; }
</style>
</head>
<body>
<main class="flyer">
  <svg class="flyer-art" width="804" height="1140" viewBox="0 0 804 1140">
    <defs>
      <linearGradient id="sky" x1="0" y1="0" x2="1" y2="1">
        <stop offset="0" stop-color="#fbefe4"/>
        <stop offset="0.35" stop-color="#e6b698"/>
        <stop offset="0.65" stop-color="#8f8590"/>
        <stop offset="1" stop-color="#3e4150"/>
      </linearGradient>
      <radialGradient id="sun" cx="0.18" cy="0.3" r="0.45">
        <stop offset="0" stop-color="#fff6e8" stop-opacity="0.95"/>
        <stop offset="1" stop-color="#fff6e8" stop-opacity="0"/>
      </radialGradient>
      <linearGradient id="band" x1="0" y1="0" x2="1" y2="0">
        <stop offset="0" stop-color="#3cc3e0"/>
        <stop offset="0.5" stop-color="#2f6fd6"/>
        <stop offset="1" stop-color="#5a4bd8"/>
      </linearGradient>
      <linearGradient id="badge" x1="0" y1="0" x2="0" y2="1">
        <stop offset="0" stop-color="#7fd6ee"/>
        <stop offset="0.3" stop-color="#1f86cf"/>
        <stop offset="0.6" stop-color="#1a55c6"/>
        <stop offset="1" stop-color="#7b55ee"/>
      </linearGradient>
      <radialGradient id="badge-shadow">
        <stop offset="0" stop-color="#000" stop-opacity="0.45"/>
        <stop offset="1" stop-color="#000" stop-opacity="0"/>
      </radialGradient>
    </defs>
    <g role="img" aria-label="Photo: hiker with backpack standing on a mountain summit at sunrise, above misty ranges">
      <rect width="804" height="760" fill="url(#sky)"/>
      <rect width="804" height="760" fill="url(#sun)"/>
    </g>
    <path d="M0,700 C200,560 450,490 804,560 L804,575 C450,520 200,600 0,730 Z" fill="url(#band)"/>
    <path d="M0,730 C200,600 450,520 804,575 L804,1140 L0,1140 Z" fill="var(--cream)"/>
    <rect x="14" y="14" width="776" height="1112" fill="none" stroke="var(--frame)" stroke-width="1"/>
    <ellipse cx="249" cy="862" rx="170" ry="14" fill="url(#badge-shadow)"/>
    <circle cx="249" cy="649" r="204" fill="url(#badge)"/>
  </svg>

  <div class="brand-name">Purely<br>Windswept</div>

  <section class="offer">
    <div class="line offer-label">OFFER CODE</div>
    <div class="line offer-code">OPENGLOW</div>
    <div class="line offer-amount">15% OFF</div>
    <div class="line offer-terms">THE BOOKERS FIRST</div>
    <div class="line offer-session">1:1 SESSION</div>
  </section>

  <section class="services">
    <h2 class="services-title">We offer</h2>
    <ul class="services-list">
      <li class="service--sessions">1:1 SESSIONS</li>
      <li class="service--workshops">WORKSHOPS</li>
      <li class="service--corporate">CORPORATE</li>
      <li class="service--corporate">TRAINING</li>
    </ul>
  </section>

  <footer class="contact">
    <p class="contact-cta">FIND OUT HOW BREATHWORK CAN HELP YOU TODAY. . .</p>
    <p class="contact-details">42 Larchfield Road, Wolverhampton. West Midlands WV10 0ZZ<br>
      <b>Tessa Orchard</b> (South): 07700 318 527 <b>Lorraine Pitt</b> (Midlands): 07700 452 183<br>
      <b>facebook</b>: /we.are.purelywindswept <b>instagram</b>: @purelywindswept</p>
    <p class="contact-web">www.purelywindswept.co.uk</p>
  </footer>
</main>
</body>
</html>
```